TALLVEX MOTOR OIL LABEL

I am launching a new motor oil product called TallVex and I would like your help in designing the packaging. The product is aimed at delivering high-performance results for vehicles, and I want the packaging to reflect the premium quality and reliability of TallVex. The design should be modern, dynamic, and appeal to car enthusiasts, while also communicating trust and innovation. I’m looking for a sleek and professional look that stands out on the shelf. Please incorporate elements that highlight its efficiency and performance, with bold typography and striking colors to grab attention.
I also need a logo for the name TallVex, and I would like your help in choosing the right colors for the packaging. The logo should be bold, memorable, and represent the strength and high performance of the product. When it comes to the packaging colors, I want something that is both eye-catching and conveys a sense of power and reliability, while also appealing to car enthusiasts. Your guidance in selecting the perfect color scheme to match the brand identity will be greatly appreciated.
The types of oils I plan to offer are available in the following sizes: 1 liter, 4 liters, and 5 liters.

• 10W40 Synthetic Blend High Mileage
• 20W50 Synthetic Blend High Mileage
• 10W30 Synthetic Blend High Mileage
• 5W30 Synthetic Blend High Mileage
• 5W20 Synthetic Blend High Mileage

Additionally, I will offer

Additionally, I will offer a
0W16 FULL SYNTHETIC
OW20 FULL SYNTHETIC
5W20 FULL SYNTHETIC
5W30 FULL SYNTHETIC
5W40 FULL SYNTHETIC
0W40 FULL SYNTHETIC
AND HD MOTOR OIL
15W40 HAVEY DUTY DIESEL ENGINE OIL SYNTHETIC BLEND
5W40 HAVEY DUTY DIESEL ENGINE OIL FULL SYNTHETIC

Font styles to use
Serif

Colors
0054AA
0677BA
7BADD7
CADEEF
E8F1F8
59FF00
82FF00
B8FF75
E3FFCB
F4FFEA
FFF300
FFF600
FEFA6F
FFFEC7
FFFEE8
FFC000
F8CF3A
FAE287
FDF2CF
FEFAEE
F0912C
F2A743
F7CA91
FBE8D2
FDF5EE
EB3D1F
EC4F4E
F09395
F8D3D4
FCEDEE

```html
<!DOCTYPE html>
<html lang="en">
<head>
<meta charset="utf-8">
<title>TallVex Motor Oil Label</title>
<link href="https://fonts.googleapis.com/css2?family=Open+Sans:wght@400;700&family=Russo+One&display=swap" rel="stylesheet">
<style>
  :root {
    --page-bg: #161618;
    --label-dark: #2f3237;
    --label-mid: #8d9096;
    --label-light: #eceef1;
    --panel-dark: #1c1f1f;
    --panel-mid: #4b5250;
    --silver: #f4f5f7;
    --brand-red: #eb3d1f;
    --badge-red: #e2202c;
    --band-red: #b0101a;
    --band-dark: #3a0508;
    --fire-deep: #1a0203;
    --fire-red: #c4140f;
    --fire-glow: #ff6a1a;
    --logo-blue: #7badd7;
    --ink: #0b0b0b;
    --white: #ffffff;
  }
  * { margin: 0; padding: 0; box-sizing: border-box; }
  html, body {
    width: 1200px; height: 1200px; overflow: hidden;
    background: var(--page-bg);
  }
  .label {
    position: absolute; left: 290px; top: 164px;
    width: 620px; height: 872px; overflow: hidden;
    background: linear-gradient(200deg, var(--label-dark) 0%, var(--label-mid) 22%, var(--label-light) 45%, #b9bbc0 60%, #2a2628 72%, var(--fire-deep) 82%);
  }
  .label__panel { position: absolute; inset: 0; }
  .label__fire {
    position: absolute; left: 0; right: 0; bottom: 0; height: 290px;
    background:
      radial-gradient(ellipse 70% 40% at 55% 100%, var(--fire-glow) 0%, rgba(255,106,26,0) 70%),
      linear-gradient(180deg, rgba(26,2,3,0) 0%, var(--fire-red) 70%, #e0281a 100%);
  }
  .badge {
    position: absolute; left: 288px; top: 121px; width: 304px; height: 37px;
    background: var(--badge-red); color: var(--white);
    font: 400 28px/37px "Russo One", sans-serif; text-align: center;
    letter-spacing: 2px; transform: skewX(-12deg);
  }
  .brand {
    position: absolute; left: 18px; top: 270px;
    font: 700 52px/1 "Open Sans", sans-serif; color: var(--logo-blue);
    letter-spacing: 1px;
  }
  .headline {
    position: absolute; left: 244px; top: 452px; width: 376px;
    font: 400 64px/1 "Russo One", sans-serif; color: var(--ink);
    letter-spacing: 6px; transform: skewX(-18deg); text-align: right;
  }
  .tagline {
    position: absolute; left: 244px; top: 514px; width: 376px; height: 90px;
    background: linear-gradient(90deg, var(--band-red) 0%, #d81f25 60%, var(--band-dark) 100%);
    color: var(--white); text-align: right; padding: 6px 14px 0 0;
    font: 400 36px/41px "Open Sans", sans-serif; letter-spacing: 4px;
  }
  .volume {
    position: absolute; left: 22px; top: 776px;
    font: 400 70px/1 "Russo One", sans-serif; color: var(--white);
    transform: skewX(-18deg); letter-spacing: 4px;
  }
</style>
</head>
<body>
  <main class="label">
    <svg class="label__panel" viewBox="0 0 620 872" width="620" height="872" aria-hidden="true">
      <defs>
        <linearGradient id="panelFill" x1="0" y1="0" x2="1" y2="1">
          <stop offset="0" stop-color="var(--panel-mid)"/>
          <stop offset="0.5" stop-color="#2a2f2e"/>
          <stop offset="1" stop-color="var(--panel-dark)"/>
        </linearGradient>
        <linearGradient id="rimFill" x1="0" y1="0" x2="1" y2="0">
          <stop offset="0" stop-color="#9a9da3"/>
          <stop offset="1" stop-color="var(--silver)"/>
        </linearGradient>
      </defs>
      <path d="M0 150 L160 102 Q180 98 196 112 L396 310 Q416 334 396 356 L0 660 Z" fill="url(#rimFill)"/>
      <path d="M0 150 L150 110 Q166 106 178 118 L360 310 Q374 330 360 348 L0 626 Z" fill="url(#panelFill)"/>
    </svg>
    <div class="label__fire" role="img" aria-label="Glowing fiery oil droplets rising from the bottom of the label"></div>
    <div class="badge">NO.1 OIL</div>
    <div class="brand">TALLVEX</div>
    <div class="headline">HIGH</div>
    <div class="tagline">Performance<br>Result</div>
    <div class="volume">5L</div>
  </main>
</body>
</html>
```